Cause bitches need love too!

I am creating an ad campaign. It will be a series of featured dogs in our shelter and they will contain a picture of the dog wich should be big enough to see on a yard sign and will change every week. I am placing the signs so that they lead you to the shelter. This is why I am also including the copy that says "you're almost there".

I have 4 tag lines:

1. Find unconditional Love.
2. She'll Love you furever!
3. He'll always listen.
4. Meet your new BFF

You're almost there 217 W Marlowe Ave
Open 10 - 7/Tues-Sat

The dimensions for the sign are 24" wide and 18" high

Every week we will have a different picture of a different dog (hopefully last week's dog gets adopted). Anyhow, I am printing out yard signs, meaning that instead of printing 160 different signs it would be ideal just to replace the photo. So far the copy that is permanent is: "You're almost there. 217 W. Marlowe Ave."

I could silhouette the image of the dog as well and super impose it on the sign, that's also a consideration, but ideally if I could have 4 tag lines I could print 40 signs of each and just replace the photo manually each week from my printer that would save costs.
Updates

Not enough designs to chose from and I edited the brief and committed to pay no matter what to increase the amount of designs as per your suggestions.

Target Market(s)

Animal lovers

Industry/Entity Type

Campaign

Font styles to use
Sans Serif

Colors

Designer to choose colors to be used in the design.

Requirements
Must have
• The dimensions for the sign are 24" wide and 18" high
Nice to have
• I want the signs to be hip, they should have a positive feel to them. You can alter the photos if you like. I am even open to new copy if you think something else works better.

```html
<!DOCTYPE html>
<html lang="en">
<head>
<meta charset="utf-8">
<title>You're Almost There – Shelter Yard Sign Series</title>
<link rel="stylesheet" href="https://fonts.googleapis.com/css2?family=Kanit:wght@700;800&family=Amatic+SC:wght@700&family=Patrick+Hand+SC&display=swap">
<style>
  :root {
    --pink: #e8175f;
    --orange: #fdb356;
    --purple: #a35fae;
    --blue: #4fb2dd;
    --white: #ffffff;
    --yellow: #f9ef3a;
    --band: #1d1919;
    --tan-light: #c98f4e;
    --tan-dark: #7a4e25;
    --coat-dark: #2b1f17;
    --grey-light: #cfc8c4;
    --grey-mid: #8d8580;
    --grey-dark: #5f5753;
  }
  * { box-sizing: border-box; margin: 0; padding: 0; }
  html, body {
    width: 1200px;
    height: 3600px;
    overflow: hidden;
    background: var(--white);
  }
  .sign-stack {
    position: relative;
    width: 1200px;
    height: 3600px;
    padding: 16px 19px 20px;
    display: grid;
    grid-template-rows: repeat(4, 876px);
    row-gap: 20px;
  }
  .sign {
    position: relative;
    width: 1162px;
    height: 876px;
    overflow: hidden;
  }
  .sign--pink { background: var(--pink); }
  .sign--orange { background: var(--orange); }
  .sign--purple { background: var(--purple); }
  .sign--blue { background: var(--blue); }

  .dog-photo {
    position: absolute;
    right: 0;
    bottom: 72px;
    width: 700px;
    height: 804px;
  }
  .dog-photo--tan {
    background: radial-gradient(ellipse 62% 70% at 62% 48%, var(--tan-light) 0%, var(--tan-dark) 48%, var(--coat-dark) 78%, rgba(43,31,23,0) 100%);
  }
  .dog-photo--grey {
    background: radial-gradient(ellipse 62% 72% at 60% 52%, var(--grey-light) 0%, var(--grey-mid) 50%, var(--grey-dark) 78%, rgba(95,87,83,0) 100%);
  }

  .tagline {
    position: absolute;
    left: 36px;
    top: 22px;
    color: var(--white);
    font-family: "Kanit", sans-serif;
    font-weight: 800;
    text-transform: uppercase;
    line-height: 0.8;
    z-index: 1;
  }
  .tagline__bold { display: block; font-size: 150px; }
  .tagline__bold--medium { font-size: 112px; line-height: 0.9; }
  .tagline__small { display: block; font-size: 56px; font-weight: 700; line-height: 1.2; margin-top: 14px; }
  .tagline__script {
    display: block;
    font-family: "Amatic SC", sans-serif;
    font-weight: 700;
    font-size: 170px;
    line-height: 0.95;
    text-transform: uppercase;
  }

  .hours {
    position: absolute;
    left: 36px;
    color: var(--yellow);
    font-family: "Kanit", sans-serif;
    font-weight: 700;
    font-size: 88px;
    line-height: 1.22;
    text-transform: uppercase;
    z-index: 1;
  }

  .direction-band {
    position: absolute;
    left: 0;
    right: 0;
    bottom: 0;
    height: 72px;
    background: var(--band);
    color: var(--white);
    font-family: "Patrick Hand SC", sans-serif;
    font-size: 44px;
    display: flex;
    align-items: center;
    justify-content: space-between;
    padding: 0 72px 0 82px;
  }
</style>
</head>
<body>
<main class="sign-stack">

  <section class="sign sign--pink">
    <div class="dog-photo dog-photo--tan" role="img" aria-label="Featured shelter dog, a tan and black shepherd mix, head tilted"></div>
    <h2 class="tagline">
      <span class="tagline__bold">She'll</span>
      <span class="tagline__bold">Love</span>
      <span class="tagline__bold">You</span>
      <span class="tagline__script">Furever!</span>
    </h2>
    <p class="hours" style="top:560px;">Open 10 - 7<br>Tues-Sat</p>
    <footer class="direction-band"><span>You're almost there</span><span>217 W Marlowe Ave</span></footer>
  </section>

  <section class="sign sign--orange">
    <div class="dog-photo dog-photo--tan" role="img" aria-label="Featured shelter dog, a tan and black shepherd mix, head tilted"></div>
    <h2 class="tagline">
      <span class="tagline__bold">Find</span>
      <span class="tagline__small">Unconditional</span>
      <span class="tagline__script">Love</span>
    </h2>
    <p class="hours" style="top:500px;">Open 10 - 7<br>Tues-Sat</p>
    <footer class="direction-band"><span>You're almost there</span><span>217 W Marlowe Ave</span></footer>
  </section>

  <section class="sign sign--purple">
    <div class="dog-photo dog-photo--grey" role="img" aria-label="Featured shelter dog, a grey and white pit bull mix looking up"></div>
    <h2 class="tagline">
      <span class="tagline__bold">He'll</span>
      <span class="tagline__bold tagline__bold--medium">Always</span>
      <span class="tagline__script">Listen</span>
    </h2>
    <p class="hours" style="top:550px;">Open 10 - 7<br>Tues-Sat</p>
    <footer class="direction-band"><span>You're almost there</span><span>217 W Marlowe Ave</span></footer>
  </section>

  <section class="sign sign--blue">
    <div class="dog-photo dog-photo--grey" role="img" aria-label="Featured shelter dog, a grey and white pit bull mix looking up"></div>
    <h2 class="tagline">
      <span class="tagline__bold">Meet</span>
      <span class="tagline__bold tagline__bold--medium">Your</span>
      <span class="tagline__bold tagline__bold--medium">New</span>
      <span class="tagline__script">BFF</span>
    </h2>
    <p class="hours" style="top:505px;">Open 10 - 7<br>Tues-Sat</p>
    <footer class="direction-band"><span>You're almost there</span><span>217 W Marlowe Ave</span></footer>
  </section>

</main>
</body>
</html>
```